professional business card

A Clean looking business card for a money transfer company. Our company is call Velorix= Transfer + Send = Transcend (next level)
to show professionalism as well as some effects to show digital tech.

1 side to have position, name and address
2 side to have company name and show that we provide money exchange and cross-border money transfer

Target Market(s)

Remittance companies and high net worth individuals

Industry/Entity Type

Finance

Contact Information for Business Card

Name, address, email, title, services- money exchange and cross-border remittance

Requirements
Nice to have
• Digital age feel

```html
<!DOCTYPE html>
<html lang="en">
<head>
<meta charset="utf-8">
<title>Velorix Business Card</title>
<link rel="stylesheet" href="https://fonts.googleapis.com/css2?family=Lato:wght@400;700;900&display=swap">
<style>
  :root {
    --backdrop: #2c2e32;
    --card-white: #ffffff;
    --navy: #243343;
    --ink: #1f2c3a;
    --cyan: #5fd2e0;
    --muted: #6b7480;
  }
  * { margin: 0; padding: 0; box-sizing: border-box; }
  html, body {
    width: 1200px; height: 952px; overflow: hidden;
    background: var(--backdrop);
    font-family: "Lato", sans-serif;
  }
  .card {
    position: absolute;
    width: 560px; height: 320px;
    border-radius: 22px;
    overflow: hidden;
    box-shadow: 0 14px 30px rgba(0,0,0,0.35);
  }
  /* Front side */
  .card--front { left: 320px; top: 110px; background: var(--card-white); color: var(--ink); }
  .brand {
    position: absolute; left: 36px; top: 34px;
    display: flex; align-items: center; gap: 12px;
  }
  .brand__mark { width: 22px; height: 22px; background: var(--cyan); }
  .brand__name {
    font-size: 30px; font-weight: 700; letter-spacing: 1px;
    text-transform: uppercase; color: var(--ink);
  }
  .contact {
    position: absolute; left: 36px; top: 130px;
    list-style: none; font-size: 11.5px; color: #3b4652; line-height: 1.35;
  }
  .contact__item { display: flex; align-items: flex-start; gap: 9px; margin-bottom: 6px; }
  .contact__icon {
    flex: none; width: 15px; height: 15px; border-radius: 3px;
    display: flex; align-items: center; justify-content: center;
    background: var(--cyan);
  }
  .contact__icon--dark { background: var(--ink); }
  .contact__icon svg { width: 10px; height: 10px; fill: #fff; }
  .person {
    position: absolute; right: 40px; top: 150px; text-align: right;
  }
  .person__name { font-size: 19px; font-weight: 700; letter-spacing: 1px; text-transform: uppercase; color: var(--ink); }
  .person__surname { color: var(--cyan); font-weight: 900; }
  .person__title { margin-top: 4px; font-size: 14px; color: var(--muted); letter-spacing: 0.5px; }
  .rule { position: absolute; height: 2px; }
  .rule--ink { left: 0; top: 250px; width: 290px; background: var(--ink); }
  .rule--cyan-front { left: 390px; top: 278px; width: 170px; background: var(--cyan); }

  /* Back side */
  .card--back { left: 320px; top: 520px; background: var(--navy); color: #fff; }
  .back-brand {
    position: absolute; left: 0; right: 0; top: 100px;
    display: flex; justify-content: center; align-items: center; gap: 14px;
  }
  .back-brand__mark { width: 26px; height: 26px; background: var(--cyan); }
  .back-brand__name {
    font-size: 40px; font-weight: 700; letter-spacing: 2px;
    text-transform: uppercase; color: var(--cyan);
  }
  .tagline {
    position: absolute; left: 0; right: 0; top: 236px;
    display: flex; align-items: center; gap: 14px;
  }
  .tagline__line { flex: 1; height: 2px; background: var(--cyan); }
  .tagline__text { font-size: 15px; letter-spacing: 0.4px; color: #f2f5f7; white-space: nowrap; }
</style>
</head>
<body>
  <section class="card card--front" aria-label="Card front">
    <div class="brand">
      <span class="brand__mark"></span>
      <span class="brand__name">Velorix</span>
    </div>

    <ul class="contact">
      <li class="contact__item">
        <span class="contact__icon contact__icon--dark">
          <svg viewBox="0 0 10 10"><path d="M5 0.5a3.2 3.2 0 0 0-3.2 3.2C1.8 6 5 9.5 5 9.5s3.2-3.5 3.2-5.8A3.2 3.2 0 0 0 5 0.5zm0 4.5a1.3 1.3 0 1 1 0-2.6 1.3 1.3 0 0 1 0 2.6z"/></svg>
        </span>
        <span>1720 Meridian Avenue<br>Arlington, VA 22201</span>
      </li>
      <li class="contact__item">
        <span class="contact__icon">
          <svg viewBox="0 0 10 10"><path d="M2.2 0.8l1.6 1.9-0.9 1.2c0.6 1.2 1.5 2.1 2.7 2.7l1.2-0.9 1.9 1.6-0.8 1.6C4.4 8.9 1.1 5.6 0.6 1.6z"/></svg>
        </span>
        <span>+00 987 654 32</span>
      </li>
      <li class="contact__item">
        <span class="contact__icon">
          <svg viewBox="0 0 10 10"><path d="M0.8 2h8.4v6H0.8zM1.5 2.6L5 5.4l3.5-2.8" stroke="#5fd2e0" stroke-width="0.8"/></svg>
        </span>
        <span>contact@velorixmail.com</span>
      </li>
      <li class="contact__item">
        <span class="contact__icon">
          <svg viewBox="0 0 10 10"><circle cx="5" cy="5" r="3.8" fill="none" stroke="#fff" stroke-width="1"/><path d="M1.2 5h7.6M5 1.2v7.6" stroke="#fff" stroke-width="0.8"/></svg>
        </span>
        <span>www.velorixtransfer.com</span>
      </li>
    </ul>

    <div class="person">
      <p class="person__name">Daniel M. <span class="person__surname">Harlow</span></p>
      <p class="person__title">Managing Director</p>
    </div>

    <span class="rule rule--ink"></span>
    <span class="rule rule--cyan-front"></span>
  </section>

  <section class="card card--back" aria-label="Card back">
    <div class="back-brand">
      <span class="back-brand__mark"></span>
      <span class="back-brand__name">Velorix</span>
    </div>
    <div class="tagline">
      <span class="tagline__line"></span>
      <span class="tagline__text">Money Exchange And Cross-border Remittance</span>
      <span class="tagline__line"></span>
    </div>
  </section>
</body>
</html>
```